Website: mentorprogram for refugees; Uplift your tomorrow

We need a website for our project Kindlo, which mainly will serve as a information site for our stakeholders. (refugees/mentees, employers/mentors, municipality and sponsors)

We also need a logo/visual design program for the project. We are thinking something green/grey/blue - close to the logo used today. The design should communicate growth, understanding/integration, knowledge. The name Kindlo comes from refugees reframing/redesigning their future as part of the concept.

Kindlo is a two-dimensional consept/program to support refugees in redesigning their future and increasing their employability. The program offers a mentor to each refugee. Mentors will be trained in the mentor-role and will be instrumental in supporting the refugees in their quest to understand work culture in Norway. Understanding of intercultural communication and the value of diversity in the workplace is an important part of the program for both parties. Nature will provide a setting for the conversations between mentor and mentee

Logo Text

Kindlo

Number of Pages Required

1 page

Font styles to use
Sans Serif

Colors
9bcb3c
0355a3
f78f20

```html
<!DOCTYPE html>
<html lang="no">
<head>
<meta charset="utf-8">
<title>Kindlo Norway</title>
<link href="https://fonts.googleapis.com/css2?family=Montserrat:wght@500;600;700&family=Open+Sans:wght@400;600;700&family=Roboto:wght@400;500;700&display=swap" rel="stylesheet">
<style>
:root{
  --green:#3aa86b;
  --green-dark:#2f9a5e;
  --mint:#e9f6ef;
  --ink:#333;
  --text:#555;
  --white:#fff;
  --footer:#2e2e2e;
  --line:#555;
}
*{box-sizing:border-box;margin:0;padding:0}
html,body{width:1200px;height:3586px;overflow:hidden}
body{position:relative;background:var(--white);font-family:"Open Sans",Arial,sans-serif;color:var(--text)}
.abs{position:absolute}
/* header */
.site-header{position:absolute;top:0;left:0;width:1200px;height:108px;background:var(--white)}
.brand{position:absolute;left:98px;top:26px;font-family:"Montserrat",Arial,sans-serif;font-weight:600;font-size:22px;letter-spacing:5px;color:var(--ink);line-height:30px}
.brand-mark{position:absolute;left:232px;top:34px;width:14px;height:14px;border-radius:50%;background:var(--green)}
.main-nav{position:absolute;right:98px;top:50px;display:flex;gap:36px;font-family:"Montserrat",Arial,sans-serif;font-weight:600;font-size:15px;color:#222}
.main-nav .active{color:var(--green)}
/* hero */
.hero{position:absolute;top:108px;left:0;width:1200px;height:474px;background:linear-gradient(100deg,#5c6a4c 0%,#7d7357 30%,#a9905d 55%,#8a8f7e 75%,#b4b8ae 100%)}
.hero-title{position:absolute;right:98px;top:118px;font-family:"Roboto",Arial,sans-serif;font-weight:700;font-size:50px;color:var(--white);letter-spacing:1px}
.hero-sub{position:absolute;right:98px;top:200px;width:420px;text-align:left;font-size:15px;font-weight:600;line-height:24px;color:var(--white)}
.hero-btn{position:absolute;right:98px;top:288px;width:132px;height:54px;background:var(--white);color:var(--green);font-family:"Montserrat",Arial,sans-serif;font-weight:600;font-size:15px;display:flex;align-items:center;justify-content:center;border-radius:3px}
.dots{position:absolute;right:98px;top:372px;display:flex;gap:6px}
.dots span{width:13px;height:13px;border:2px solid var(--white);border-radius:50%}
.dots span.on{background:var(--green);border-color:var(--white)}
/* about */
.welcome{left:98px;top:656px;font-size:21px;color:var(--ink)}
.h-green{font-family:"Roboto",Arial,sans-serif;font-weight:700;color:var(--green);font-size:26px;letter-spacing:.5px}
.about-title{left:98px;top:693px}
.body-copy{font-size:13px;line-height:23px;color:var(--text)}
.about-copy{left:98px;top:744px;width:550px}
.btn{position:absolute;height:50px;background:var(--green);color:var(--white);font-family:"Montserrat",Arial,sans-serif;font-weight:600;font-size:15px;display:flex;align-items:center;justify-content:center}
.about-photo{left:673px;top:652px;width:427px;height:314px;border:2px solid #ddd;background:linear-gradient(160deg,#9bb3c4 0%,#c9c7b8 40%,#8c7a55 70%,#5a5040 100%)}
/* topics */
.topics{position:absolute;top:1035px;left:0;width:1200px;height:497px;background:var(--green)}
.topics-title{position:absolute;top:54px;width:1200px;text-align:center;font-family:"Roboto",Arial,sans-serif;font-weight:500;font-size:27px;color:var(--white)}
.topics-rule{position:absolute;top:104px;left:548px;width:104px;height:3px;background:var(--white)}
.topic{position:absolute;top:170px;width:190px;text-align:center}
.topic svg{display:block;margin:0 auto}
.topic p{margin-top:14px;font-family:"Roboto",Arial,sans-serif;font-weight:700;font-size:16px;line-height:24px;color:var(--white)}
.arrow{position:absolute;top:284px}
/* split sections */
.sec-title{font-family:"Roboto",Arial,sans-serif;font-weight:700;color:var(--green);font-size:23px;letter-spacing:.5px}
.photo{position:absolute}
.bullets{list-style:none}
.bullets li{position:relative;padding-left:22px;margin-bottom:12px}
.bullets li::before{content:"";position:absolute;left:0;top:6px;width:9px;height:9px;border:2px solid var(--green);border-radius:50%}
.bold{font-weight:700;color:var(--ink)}
.sub-green{font-size:16px;color:var(--green);font-weight:600}
.two-col{display:grid;grid-template-columns:130px 300px;row-gap:14px;font-size:14px;color:var(--ink)}
.two-col span{position:relative;padding-left:22px;white-space:nowrap}
.two-col span::before{content:"";position:absolute;left:0;top:5px;width:9px;height:9px;border:2px solid var(--green);border-radius:50%}
/* blog */
.blog{position:absolute;top:2736px;left:0;width:1200px;height:450px;background:var(--mint)}
.blog-title{position:absolute;top:38px;width:1200px;text-align:center;font-family:"Roboto",Arial,sans-serif;font-weight:500;font-size:27px;color:var(--green)}
.blog-rule{position:absolute;top:86px;left:556px;width:88px;height:3px;background:var(--green)}
.post-img{position:absolute;top:156px;width:247px;height:206px;border:3px solid var(--white)}
.post-title{position:absolute;top:158px;font-family:"Roboto",Arial,sans-serif;font-weight:500;font-size:16px;color:var(--ink)}
.post-copy{position:absolute;top:192px;width:218px;font-size:11.5px;line-height:20px;text-align:justify;color:var(--text)}
/* footer */
.site-footer{position:absolute;top:3186px;left:0;width:1200px;height:400px;background:var(--footer);color:var(--white)}
.badge{position:absolute;top:64px;width:106px;height:74px;background:var(--white);border-radius:4px;display:flex;align-items:center;justify-content:center}
.contact{position:absolute;top:180px;width:1200px;display:flex;justify-content:center;gap:40px;font-size:19px;align-items:center}
.contact span{display:flex;align-items:center;gap:12px}
.foot-nav{position:absolute;top:266px;width:1200px;display:flex;justify-content:center;gap:26px;font-family:"Montserrat",Arial,sans-serif;font-size:15px;font-weight:500}
.foot-line{position:absolute;top:320px;left:98px;width:1004px;height:1px;background:var(--line)}
.copyright{position:absolute;top:354px;left:98px;font-size:13px}
.social{position:absolute;top:344px;right:98px;display:flex;gap:8px}
.social span{width:34px;height:34px;border:2px solid var(--white);border-radius:50%}
</style>
</head>
<body>

<header class="site-header">
  <div class="brand">Kindlo<br>Norway</div>
  <span class="brand-mark"></span>
  <nav class="main-nav">
    <span class="active">HOME</span><span>ABOUT US</span><span>OUR PROJECTS</span><span>BLOG</span><span>TOPICS COVERED</span><span>CONTACT</span>
  </nav>
</header>

<section class="hero" role="img" aria-label="Photo of refugees walking along a field path carrying bags">
  <h1 class="hero-title">KINDLO NORWAY</h1>
  <p class="hero-sub">Be instrumental in supporting the refugees in their quest to understand work culture in Norway</p>
  <a class="hero-btn">READ MORE</a>
  <div class="dots"><span></span><span></span><span></span><span></span><span class="on"></span></div>
</section>

<section>
  <p class="abs welcome">Welcome</p>
  <h2 class="abs h-green about-title">ABOUT KINDLO</h2>
  <div class="abs about-copy body-copy">
    <p>KINDLO is an architectural practice that focuses on innovative problem solving based on existing premises, by focusing on simple and effective alternatives. The approach is based on Brightfold method : Design Thinking and Human Centered Design.</p>
    <p style="margin-top:14px">A two-dimensional consept to support refugees in redesigning their future and increasing their employability.</p>
  </div>
  <a class="btn" style="left:98px;top:907px;width:131px">READ MORE</a>
  <div class="abs about-photo" role="img" aria-label="Photo of volunteers handing out supplies at a camp"></div>
</section>

<section class="topics">
  <h2 class="topics-title">TOPICS COVERED</h2>
  <span class="topics-rule"></span>
  <svg class="arrow" style="left:30px" width="26" height="46" viewBox="0 0 26 46"><path d="M22 4 L5 23 L22 42" fill="none" stroke="#fff" stroke-width="3"/></svg>
  <svg class="arrow" style="right:30px" width="26" height="46" viewBox="0 0 26 46"><path d="M4 4 L21 23 L4 42" fill="none" stroke="#fff" stroke-width="3"/></svg>

  <div class="topic" style="left:58px">
    <svg width="140" height="150" viewBox="0 0 140 150"><circle cx="70" cy="68" r="62" fill="none" stroke="#fff" stroke-width="3"/><path d="M61 129 L70 142 L79 129" fill="#3aa86b" stroke="#fff" stroke-width="3"/><circle cx="70" cy="54" r="14" fill="#fff"/><path d="M44 98c0-18 12-28 26-28s26 10 26 28z" fill="#fff"/></svg>
    <p>Training for<br>mentoring skills</p>
  </div>
  <div class="topic" style="left:268px">
    <svg width="140" height="150" viewBox="0 0 140 150"><circle cx="70" cy="68" r="62" fill="#fff" stroke="#fff" stroke-width="3"/><path d="M61 129 L70 142 L79 129" fill="#fff" stroke="#fff" stroke-width="3"/><circle cx="70" cy="68" r="56" fill="none" stroke="#3aa86b" stroke-width="2"/><path d="M70 90 48 68a13 13 0 0 1 22-16 13 13 0 0 1 22 16z" fill="#3aa86b"/></svg>
    <p>Understanding<br>organizational<br>diversity</p>
  </div>
  <div class="topic" style="left:478px">
    <svg width="140" height="150" viewBox="0 0 140 150"><circle cx="70" cy="68" r="62" fill="none" stroke="#fff" stroke-width="3"/><path d="M61 129 L70 142 L79 129" fill="#3aa86b" stroke="#fff" stroke-width="3"/><circle cx="70" cy="58" r="18" fill="#fff"/><path d="M58 72 52 98l12-6 6 10 6-10 12 6-6-26z" fill="#fff"/></svg>
    <p>Building trust in a<br>diverse culture</p>
  </div>
  <div class="topic" style="left:688px">
    <svg width="140" height="150" viewBox="0 0 140 150"><circle cx="70" cy="68" r="62" fill="none" stroke="#fff" stroke-width="3"/><path d="M61 129 L70 142 L79 129" fill="#3aa86b" stroke="#fff" stroke-width="3"/><rect x="58" y="44" width="24" height="12" rx="3" fill="none" stroke="#fff" stroke-width="4"/><rect x="42" y="54" width="56" height="38" rx="4" fill="#fff"/><rect x="42" y="68" width="56" height="3" fill="#3aa86b"/></svg>
    <p>Understanding of<br>basic Norwegian<br>work</p>
  </div>
  <div class="topic" style="left:898px">
    <svg width="140" height="150" viewBox="0 0 140 150"><circle cx="70" cy="68" r="62" fill="none" stroke="#fff" stroke-width="3"/><path d="M61 129 L70 142 L79 129" fill="#3aa86b" stroke="#fff" stroke-width="3"/><path d="M52 98V82c-8-6-10-14-10-22 0-18 14-28 30-28s28 12 28 26l6 12h-6v10h-12v18z" fill="none" stroke="#fff" stroke-width="4"/><circle cx="70" cy="60" r="9" fill="#fff"/></svg>
    <p>Psychological<br>contracts in<br>Norwegian worklife</p>
  </div>
</section>

<section>
  <h2 class="abs sec-title" style="left:98px;top:1604px">THE MENTORS WILL</h2>
  <span class="abs" style="left:98px;top:1644px;width:78px;height:3px;background:var(--green)"></span>
  <ul class="abs bullets body-copy" style="left:98px;top:1666px;width:440px">
    <li>Be instrumental in supporting the refugees in their quest to under stand work culture in Norway.</li>
    <li>Get mentor training, a deepened understanding of intercultural communication and the value of diversity in the workplace.<br><span class="bold">Nature will provide a setting for the conversations between mentor and mentee.</span></li>
  </ul>
  <a class="btn" style="left:122px;top:1852px;width:114px;height:44px;font-size:14px">READ MORE</a>
  <div class="photo" style="left:600px;top:1532px;width:600px;height:392px;background:linear-gradient(130deg,#6c6a66 0%,#9a8574 40%,#7a3a2e 70%,#4a4a4e 100%);clip-path:polygon(0 24px,100% 0,100% 100%,0 100%)" role="img" aria-label="Photo of a young refugee sitting among a crowd"></div>
  <svg class="abs" style="left:600px;top:1714px" width="16" height="32" viewBox="0 0 16 32"><path d="M0 0 16 16 0 32z" fill="#fff"/></svg>
</section>

<section>
  <div class="photo" style="left:0;top:1918px;width:600px;height:396px;background:linear-gradient(120deg,#8a3a34 0%,#c2553f 30%,#3f5e7a 60%,#b9bcc4 100%);clip-path:polygon(0 0,100% 0,100% 100%,0 calc(100% - 30px))" role="img" aria-label="Photo of people at a demonstration holding flags"></div>
  <svg class="abs" style="left:584px;top:2110px" width="16" height="32" viewBox="0 0 16 32"><path d="M16 0 0 16 16 32z" fill="#fff"/></svg>
  <h2 class="abs sec-title" style="left:643px;top:1970px">PROGRAM-INNHOLD</h2>
  <span class="abs" style="left:643px;top:2010px;width:78px;height:3px;background:var(--green)"></span>
  <div class="abs body-copy" style="left:643px;top:2032px;width:460px">
    <p style="font-size:14px;color:var(--ink)">Kindlo Norway består av to programmer somhar noe</p>
    <p class="bold" style="margin-top:8px;font-size:14px">Selv-ledelses program for flyktninger</p>
    <p>Et 5-7 modulers program over 1 år (à 2-3 dager) med stor grad av indivi duell tilpasning. Det overordnede programmet tilpasses den enkelte kommune basert på deres eksisterende integreringsarbeid.</p>
    <p class="bold" style="margin-top:16px;font-size:14px">Kindlo mentorprogram</p>
    <p>Et 3-4 modulers program der ledere/fagpersoner fra lokale organisas joner (privat eller offentlig sektor) etter avtale med.</p>
  </div>
</section>

<section>
  <h2 class="abs sec-title" style="left:98px;top:2370px">HVORFOR KINDLO</h2>
  <span class="abs" style="left:98px;top:2410px;width:78px;height:3px;background:var(--green)"></span>
  <p class="abs body-copy" style="left:98px;top:2428px;width:470px">Vellykket integrering av flyktninger i arbeidslivet krever kompetanse og riktig mindset hos både flyktninger og arbeidsgivere. Kindlo vil jobbe på 'begge sider av bordet' der mentorene vil være brobyggere og bidra til at flyktninger lykkes.</p>
  <p class="abs sub-green" style="left:98px;top:2540px">Hvem deltar og bidrar</p>
  <div class="abs two-col" style="left:98px;top:2582px">
    <span>Flyktninger</span><span>Mentorer fra lokale arbeidsgivere</span>
    <span>FKommunene</span><span>Lumora</span>
  </div>
  <div class="photo" style="left:600px;top:2306px;width:600px;height:430px;background:linear-gradient(170deg,#b7c2c8 0%,#9aa07a 35%,#6f7a4e 60%,#6a6a6a 85%,#505050 100%);clip-path:polygon(0 20px,100% 0,100% calc(100% - 40px),0 100%)" role="img" aria-label="Photo of refugees walking along a road with backpacks"></div>
  <svg class="abs" style="left:600px;top:2500px" width="16" height="32" viewBox="0 0 16 32"><path d="M0 0 16 16 0 32z" fill="#fff"/></svg>
</section>

<section class="blog">
  <h2 class="blog-title">OUR BLOG POSTS</h2>
  <span class="blog-rule"></span>

  <div class="post-img" style="left:100px;background:linear-gradient(150deg,#a9c0d2,#6f7a86 50%,#c7a03a 80%,#4a4a4a)" role="img" aria-label="Photo of volunteers helping refugees at a station"></div>
  <h3 class="post-title" style="left:368px">NEQUE PORRO QUISQUAM</h3>
  <p class="post-copy" style="left:368px">Nemo enim ipsam voluptatem quia voluptas sit aspernatur aut odit aut fugit, sed quia consequuntur magni dolores eos qui ratione voluptatem sequi nesciunt.</p>
  <a class="btn" style="left:368px;top:3054px;width:106px;height:38px;font-size:13px">CLICK HERE</a>

  <div class="post-img" style="left:619px;background:linear-gradient(150deg,#7a6a5e,#a87c62 45%,#c9c33e 70%,#4d4b48)" role="img" aria-label="Photo of a crowd of refugees receiving help"></div>
  <h3 class="post-title" style="left:887px">NEMO ENIM IPSAM</h3>
  <p class="post-copy" style="left:887px">Nemo enim ipsam voluptatem quia voluptas sit aspernatur aut odit aut fugit, sed quia consequuntur magni dolores eos qui ratione voluptatem sequi nesciunt.</p>
  <a class="btn" style="left:887px;top:3054px;width:106px;height:38px;font-size:13px">CLICK HERE</a>
</section>

<footer class="site-footer">
  <div class="badge" style="left:482px"><span style="width:40px;height:40px;background:#d9d9d9;border-radius:4px"></span></div>
  <div class="badge" style="left:610px"><span style="width:44px;height:44px;border:2px solid #9aa3c4;border-radius:50%"></span></div>
  <div class="contact">
    <span><svg width="32" height="32" viewBox="0 0 32 32"><circle cx="16" cy="16" r="14" fill="none" stroke="#fff" stroke-width="2"/><rect x="9" y="11" width="14" height="10" fill="none" stroke="#fff" stroke-width="1.8"/><path d="M9 11l7 6 7-6" fill="none" stroke="#fff" stroke-width="1.8"/></svg>info@kindlo.no</span>
    <span><svg width="32" height="32" viewBox="0 0 32 32"><circle cx="16" cy="16" r="14" fill="none" stroke="#fff" stroke-width="2"/><path d="M11 9l3 0 2 4-2 2a10 10 0 0 0 4 4l2-2 4 2v3c-8 1-14-5-13-13z" fill="#fff"/></svg>180 555 0199</span>
  </div>
  <nav class="foot-nav">
    <span>HOME</span><span>|</span><span>ABOUT US</span><span>|</span><span>OUR PROJECTS</span><span>|</span><span>TOPICS COVERED</span><span>|</span><span>BLOG</span><span>|</span><span>CONTACT US</span>
  </nav>
  <span class="foot-line"></span>
  <p class="copyright">Copyright © 2017 Kindlo Norway. All Right Reserved</p>
  <div class="social"><span></span><span></span><span></span><span></span><span></span></div>
</footer>

</body>
</html>
```